Letterhead & Greeting Card Design Project

I need a few files prepared for dynamic digital printing: letterhead and 2 postcards with an envelope for each. Enclosed are specific directions from the printer for each file and overall. I have also enclosed mockups of what I would like on those designs and some raw files to work with.

Industry/Entity Type

Digital

```html
<!DOCTYPE html>
<html lang="en">
<head>
<meta charset="UTF-8">
<title>Envelope</title>
<link rel="stylesheet" href="https://fonts.googleapis.com/css2?family=Titillium+Web:wght@400&display=swap">
<style>
  :root {
    --paper: #ffffff;
    --ink: #1f1f1f;
    --dot-grey: #a9a9a9;
    --dot-blue: #7cc6e2;
  }
  html, body {
    margin: 0;
    padding: 0;
    overflow: hidden;
    background: var(--paper);
  }
  .envelope {
    position: relative;
    width: 1200px;
    height: 701px;
    background: var(--paper);
    overflow: hidden;
    font-family: "Titillium Web", sans-serif;
    color: var(--ink);
  }
  .return-address {
    position: absolute;
    left: 66px;
    top: 42px;
    margin: 0;
    font-size: 31px;
    line-height: 39px;
    font-style: normal;
  }
  .recipient-address {
    position: absolute;
    left: 400px;
    top: 340px;
    margin: 0;
    font-size: 31px;
    line-height: 50px;
    font-style: normal;
  }
  .dot-cluster {
    position: absolute;
    left: 0;
    bottom: 0;
    width: 240px;
    height: 160px;
    background:
      radial-gradient(ellipse at 30% 45%, rgba(169,169,169,0.55) 0%, rgba(169,169,169,0) 60%),
      radial-gradient(ellipse at 72% 75%, rgba(124,198,226,0.6) 0%, rgba(124,198,226,0) 55%);
  }
</style>
</head>
<body>
  <main class="envelope">
    <address class="return-address">
      John Doe<br>
      Company<br>
      Street<br>
      City, State/Province, Zip/Postal Code
    </address>

    <address class="recipient-address">
      Jane Jones<br>
      Account Name<br>
      Street<br>
      City, State/Province, Zip/Postal Code
    </address>

    <div class="dot-cluster" role="img" aria-label="Decorative cluster of grey and light blue dots"></div>
  </main>
</body>
</html>
```